Restaurant needs a vertical banner for fried catfish

Our restaurant is looking for an eye-catching 78.75in. x 36in. vertical physical banner ad for our fried catfish. Photos for the fried catfish will be provided as a reference but we will also accept anything similar to the photo. We will be using the following as our receptacle: https://www.plankoria.example/banner-stand/retractable-banner-stands/
The design must incorporate the following flavor texts:
Fried Catfish
Always Fresh!
Made from Scratch
Hand-cut Fillets
The Best Catfish in Texas
Served with fries, hush puppies, and a 32oz fountain drink
Also available by the pound!
The final design should be creative, professional, and eye-catching for customers.
Updates
Colors
Designer to choose colors to be used in the design.
Requirements
Must have
- We are open to any and all design elements, albeit the 'flavor texts' should not overpower, but complement the fried catfish photo. 'Fried Catfish' can be used in lieu of a main title/logo.
Nice to have
- Transparent or textured backgrounds that can encompass any or all part of the banner such as a cutting board, shadows, abstract, etc to show depth are a plus.
- Use of vectors or objects such as ribbons or shapes to encapsulate the 'flavor texts' are also encouraged.

```html
<!DOCTYPE html>
<html lang="en">
<head>
<meta charset="utf-8">
<title>Fried Catfish Banner</title>
<link href="https://fonts.googleapis.com/css2?family=Raleway:wght@500;600;700;800&display=swap" rel="stylesheet">
<style>
  :root {
    --page: #f1f1f3;
    --ink: #23252b;
    --gold: #fbb914;
    --amber: #f9a41f;
    --deep-amber: #f6911e;
    --pale-gold: #fdc31a;
    --accent: #f7c21b;
  }
  * { margin: 0; padding: 0; box-sizing: border-box; }
  html, body { width: 1200px; height: 1200px; overflow: hidden; }
  body {
    background: var(--page);
    font-family: "Raleway", sans-serif;
    color: var(--ink);
    position: relative;
  }
  .banner {
    position: absolute;
    left: 340px;
    top: 30px;
    width: 521px;
    height: 1140px;
    overflow: hidden;
    background: var(--amber);
  }
  .banner__header, .banner__footer {
    position: absolute;
    left: 0;
    width: 100%;
    background: var(--ink);
    text-align: center;
    color: var(--accent);
    z-index: 3;
  }
  .banner__header { top: 0; height: 56px; padding-top: 17px; }
  .banner__header-title { font-size: 9.5px; font-weight: 700; letter-spacing: 0.1px; }
  .banner__header-url { font-size: 5px; font-weight: 600; margin-top: 2px; letter-spacing: 0.1px; }
  .banner__footer {
    bottom: 0; height: 55px;
    display: flex; align-items: center; justify-content: center; gap: 5px;
    font-size: 6px; font-weight: 700;
  }
  .banner__footer-name { font-size: 8px; font-weight: 700; }
  .banner__photo {
    position: absolute;
    left: 0; top: 56px;
    width: 100%; height: 290px;
    background:
      radial-gradient(ellipse at 50% 50%, #b8732b 0%, #9a5a22 35%, transparent 60%),
      radial-gradient(ellipse at 85% 70%, #e9c070 0%, transparent 45%),
      linear-gradient(160deg, #c9b48a 0%, #e8e4dc 30%, #a86a30 60%, #d9ae62 100%);
    z-index: 1;
  }
  .banner__facets { position: absolute; left: 0; top: 0; z-index: 2; }
  .banner__copy {
    position: absolute;
    left: 0; top: 0; width: 100%; height: 100%;
    text-align: center;
    z-index: 3;
  }
  .banner__title {
    position: absolute; left: 0; width: 100%;
    top: 522px;
    font-size: 55px; font-weight: 800; line-height: 1; letter-spacing: -0.5px;
    white-space: nowrap;
  }
  .banner__subtitle {
    position: absolute; left: 0; width: 100%;
    top: 591px;
    font-size: 38px; font-weight: 700; line-height: 1;
  }
  .banner__rule {
    position: absolute; left: 216px; top: 643px;
    width: 90px; height: 5px; background: var(--ink);
  }
  .banner__point {
    position: absolute; left: 0; width: 100%;
    font-size: 22.5px; font-weight: 500; line-height: 1;
  }
  .banner__point--scratch { top: 720px; }
  .banner__point--fillets { top: 762px; }
  .banner__point--texas { top: 804px; }
  .banner__note {
    position: absolute; left: 0; width: 100%;
    top: 846px; font-size: 13.5px; font-weight: 500; line-height: 1;
  }
  .banner__pound {
    position: absolute; left: 0; width: 100%;
    top: 881px; font-size: 19px; font-weight: 500; line-height: 1;
  }
</style>
</head>
<body>
  <main class="banner">
    <header class="banner__header">
      <p class="banner__header-title">VISIT OUR WEBSITE</p>
      <p class="banner__header-url">WWW.BAYOUFRYHOUSE.EXAMPLE</p>
    </header>

    <div class="banner__photo" role="img" aria-label="Photo of a plate of fried catfish fillets with fries, hush puppies, tartar sauce and tomatoes"></div>

    <svg class="banner__facets" width="521" height="1140" viewBox="0 0 521 1140" aria-hidden="true">
      <polygon points="0,310 440,330 521,262 521,1085 0,1085" fill="var(--amber)"/>
      <polygon points="0,310 80,312 0,390" fill="var(--pale-gold)"/>
      <polygon points="80,312 440,330 340,424 70,360" fill="var(--gold)"/>
      <polygon points="440,330 521,262 521,410 340,424" fill="var(--deep-amber)"/>
      <polygon points="340,424 521,410 521,1085 440,1085 380,760" fill="var(--gold)" opacity="0.9"/>
      <polygon points="0,390 70,360 340,424 0,700" fill="#f8a31d"/>
      <polygon points="0,700 340,424 380,760 440,1085 190,1085 0,960" fill="#fab01a" opacity="0.6"/>
      <polygon points="0,960 190,1085 0,1085" fill="var(--deep-amber)" opacity="0.7"/>
      <polygon points="400,1085 521,990 521,1085" fill="var(--deep-amber)" opacity="0.6"/>
    </svg>

    <section class="banner__copy">
      <h1 class="banner__title">FRIED CATFISH</h1>
      <h2 class="banner__subtitle">ALWAYS FRESH!</h2>
      <div class="banner__rule"></div>
      <p class="banner__point banner__point--scratch">MADE FROM SCRATCH</p>
      <p class="banner__point banner__point--fillets">HAND-CUT FILLETS</p>
      <p class="banner__point banner__point--texas">THE BEST CATFISH IN TEXAS</p>
      <p class="banner__note">SERVED WITH FRIES, HUSH PUPPIES, AND A 32OZ FOUNTAIN DRINK</p>
      <p class="banner__pound">ALSO AVAILABLE BY THE POUND!</p>
    </section>

    <footer class="banner__footer">
      <span>MORE INFO:</span>
      <span class="banner__footer-name">BAYOU FRY HOUSE</span>
    </footer>
  </main>
</body>
</html>
```